依頼詳細
12月下旬~1月上旬オープンに向けてのチラシ作成をお願いいたします。オープン以降も同じチラシを定期的にポスティングいたしますので汎用できるようにお願いいたします。
納品はaiデータでお願いいたします。
記載項目
社名や電話番号は後で投稿させていただきます。
サイズ
A4
ページ数
片面
希望イメージ
シンプル 複雑
単色 カラフル
暗い 明るい
日常 高級
遊び心 厳粛
未来的 伝統的
女性的 男性的
希望する色
水色系
納品ファイル
• イラストレーター形式 (.ai)
補足説明
脱毛サロンのロゴを貼り付けさせていただきます。
脱毛器の画像や使用イメージ画像を追加させていただきます。
よろしくお願いいたします。
作成していただいているところに追記すみません。
オープン期間限定キャンペーン→その後、通常価格に戻します。
メニュー内容につきましては
30分→通常3500円
60分→通常4500円
月額会員→通常5500円(初月のみ)
全メニュー1000円off!!
ずーっと会員登録費・事務手数料【無料】
■ 選んだ理由

わかりやすさ。色合い

■ 提案者全員のお礼・コメント

今回たくさんのご応募いただきありがとうございます。
また、どの提案も素敵なもので決めるのに苦慮しました。またよろしくお願いいたします。

```html
<!DOCTYPE html>
<html lang="ja">
<head>
<meta charset="utf-8">
<title>セルフ脱毛サロン OPEN チラシ</title>
<link rel="stylesheet" href="https://fonts.googleapis.com/css2?family=M+PLUS+Rounded+1c:wght@500;700;800;900&family=Noto+Sans+JP:wght@400;500;700&display=swap">
<style>
  :root {
    --pink: #ef8798;
    --pink-soft: #f7b3bf;
    --blue: #4fb3df;
    --blue-deep: #2d9bcf;
    --blue-pale: #dff1fa;
    --yellow: #f7d64a;
    --ink: #555a60;
    --white: #ffffff;
  }
  * { margin: 0; padding: 0; box-sizing: border-box; }
  html, body { width: 849px; height: 1200px; overflow: hidden; background: var(--white); }
  body { font-family: "Noto Sans JP", sans-serif; color: var(--ink); }
  .flyer { position: relative; width: 849px; height: 1200px; overflow: hidden; background: var(--white); }

  .hero-photo {
    position: absolute; left: 0; top: 0; width: 849px; height: 560px;
    background: linear-gradient(160deg, #f4f1ee 0%, #ebe4df 45%, #e2d7d0 70%, #f3efec 100%);
  }
  .hero-note {
    position: absolute; left: 650px; top: 20px; width: 180px;
    font-size: 12px; line-height: 1.55; color: var(--ink);
  }
  .salon-tag {
    position: absolute; left: 32px; top: 132px;
    background: var(--pink); color: var(--white);
    font-family: "M PLUS Rounded 1c", sans-serif; font-weight: 800;
    font-size: 37px; letter-spacing: 1px;
    padding: 6px 26px 8px; border-radius: 40px;
  }
  .open-title {
    position: absolute; left: 22px; top: 185px;
    font-family: "M PLUS Rounded 1c", sans-serif; font-weight: 900;
    font-size: 128px; line-height: 1; letter-spacing: 2px;
    color: var(--pink);
  }
  .open-date {
    position: absolute; left: 52px; top: 410px; width: 140px; height: 140px;
    border-radius: 50%; background: var(--yellow);
    display: flex; flex-direction: column; align-items: center; justify-content: center;
    font-family: "M PLUS Rounded 1c", sans-serif; font-weight: 800; color: var(--blue-deep);
    transform: rotate(-8deg);
  }
  .open-date .day { font-size: 42px; line-height: 1; }
  .open-date .week { font-size: 18px; margin-top: 2px; }

  .family-art {
    position: absolute; left: 430px; top: 380px; width: 390px; height: 220px;
    background: linear-gradient(180deg, #fde9d6 0%, #f6c9a6 55%, #c9dbe9 100%);
    border-radius: 20px 20px 0 0; opacity: .9;
  }

  .kids-band {
    position: absolute; left: 0; top: 600px; width: 849px; height: 80px;
    background: repeating-linear-gradient(135deg, var(--blue-pale) 0 14px, #cfe9f6 14px 28px);
    display: flex; align-items: center; justify-content: center;
  }
  .kids-band h2 {
    font-family: "M PLUS Rounded 1c", sans-serif; font-weight: 900;
    font-size: 50px; color: var(--blue);
    -webkit-text-stroke: 10px var(--white); paint-order: stroke fill;
    letter-spacing: 2px;
  }

  .worry-lead {
    position: absolute; left: 0; top: 692px; width: 849px; text-align: center;
    font-family: "M PLUS Rounded 1c", sans-serif; font-weight: 700; font-size: 22px; color: var(--ink);
  }
  .worries {
    position: absolute; left: 48px; top: 728px; width: 760px;
    display: flex; justify-content: space-between;
  }
  .worry {
    width: 178px; height: 74px; border-radius: 38px; background: #fde6ea;
    display: flex; align-items: center; gap: 6px; padding: 0 14px;
    font-size: 15px; font-weight: 500; line-height: 1.35; color: var(--ink);
  }
  .worry svg { flex: 0 0 22px; }

  .device-photo {
    position: absolute; left: 36px; top: 820px; width: 220px; height: 310px;
    background: linear-gradient(180deg, #f1f3f5 0%, #dfe4e8 60%, #c9d0d6 100%);
    border-radius: 12px;
  }
  .first-badge {
    position: absolute; left: 190px; top: 870px; width: 78px; height: 78px; border-radius: 50%;
    background: var(--yellow); color: var(--blue-deep);
    display: flex; align-items: center; justify-content: center;
    font-family: "M PLUS Rounded 1c", sans-serif; font-weight: 800; font-size: 21px;
  }
  .safety-copy {
    position: absolute; left: 290px; top: 852px;
    font-family: "M PLUS Rounded 1c", sans-serif; font-weight: 800; color: var(--blue-deep);
    font-size: 34px; line-height: 1.3; letter-spacing: 1px;
  }
  .features {
    position: absolute; left: 296px; top: 960px; display: flex; gap: 26px;
  }
  .feature { width: 78px; text-align: center; }
  .feature .icon {
    width: 78px; height: 78px; border-radius: 50%; background: var(--pink);
    display: flex; align-items: center; justify-content: center;
  }
  .feature p { margin-top: 8px; font-size: 14px; font-weight: 700; color: var(--ink); white-space: nowrap; }

  .usage-arc { position: absolute; left: 612px; top: 818px; }
  .usage-photo {
    position: absolute; left: 640px; top: 866px; width: 170px; height: 170px; border-radius: 50%;
    background: radial-gradient(circle at 45% 45%, #f8efe9 0%, #ead8cd 60%, #d9c3b6 100%);
  }

  .contact-bar {
    position: absolute; left: 0; top: 1120px; width: 849px; height: 80px;
    border-top: 3px solid var(--blue);
  }
  .brand {
    position: absolute; left: 40px; top: 1140px; display: flex; align-items: center; gap: 10px;
    font-family: "M PLUS Rounded 1c", sans-serif; font-weight: 700; font-size: 30px; color: var(--blue);
  }
  .brand .dot { width: 14px; height: 14px; border-radius: 50%; background: var(--blue); }
  .contact {
    position: absolute; left: 300px; top: 1128px; text-align: left;
  }
  .contact .label { font-size: 13px; font-weight: 700; color: var(--blue-deep); }
  .contact .tel {
    display: flex; align-items: center; gap: 6px;
    font-family: "M PLUS Rounded 1c", sans-serif; font-weight: 800; font-size: 30px; color: var(--blue-deep); line-height: 1.15;
  }
  .contact .address { font-size: 11px; color: var(--ink); }
  .map-box {
    position: absolute; left: 625px; top: 1116px; width: 200px; height: 74px;
    border: 1.5px solid #9aa3ab; background: #f3f5f7;
    display: flex; align-items: center; justify-content: center; font-size: 12px; color: var(--ink);
  }
</style>
</head>
<body>
<div class="flyer">
  <div class="hero-photo" role="img" aria-label="素肌の脚をそっとなでる女性の写真"></div>
  <p class="hero-note">毛の成長はホルモンが関係しているため、生活習慣の乱れやストレスなども毛の濃さや成長スピードに影響するといわれています。</p>
  <div class="salon-tag">セルフ脱毛サロン</div>
  <h1 class="open-title">OPEN!</h1>
  <div class="open-date"><span class="day">00/00</span><span class="week">sun</span></div>
  <div class="family-art" role="img" aria-label="笑顔の親子4人のイラスト"></div>

  <div class="kids-band"><h2>子供も脱毛できる!</h2></div>

  <p class="worry-lead">このようなお悩みございませんか?</p>
  <div class="worries">
    <div class="worry"><svg width="22" height="22" viewBox="0 0 22 22"><path d="M3 11l5 5 11-11" fill="none" stroke="#ef8798" stroke-width="3" stroke-linecap="round" stroke-linejoin="round"/></svg><span>毛が濃くて<br>悩んでいる</span></div>
    <div class="worry"><svg width="22" height="22" viewBox="0 0 22 22"><path d="M3 11l5 5 11-11" fill="none" stroke="#ef8798" stroke-width="3" stroke-linecap="round" stroke-linejoin="round"/></svg><span>周りから<br>指摘された</span></div>
    <div class="worry"><svg width="22" height="22" viewBox="0 0 22 22"><path d="M3 11l5 5 11-11" fill="none" stroke="#ef8798" stroke-width="3" stroke-linecap="round" stroke-linejoin="round"/></svg><span>体育の授業など<br>肌を出したくない</span></div>
    <div class="worry"><svg width="22" height="22" viewBox="0 0 22 22"><path d="M3 11l5 5 11-11" fill="none" stroke="#ef8798" stroke-width="3" stroke-linecap="round" stroke-linejoin="round"/></svg><span>脱毛に抵抗があり<br>肌荒れが心配</span></div>
  </div>

  <div class="device-photo" role="img" aria-label="脱毛機器の写真"></div>
  <div class="first-badge">県内初</div>
  <p class="safety-copy">子供も脱毛できる<br>安心安全な機材</p>
  <div class="features">
    <div class="feature">
      <div class="icon"><svg width="38" height="38" viewBox="0 0 38 38"><path d="M6 20l8 8 18-18" fill="none" stroke="#fff" stroke-width="4" stroke-linecap="round" stroke-linejoin="round"/></svg></div>
      <p>操作が簡単</p>
    </div>
    <div class="feature">
      <div class="icon"><svg width="38" height="38" viewBox="0 0 38 38"><path d="M19 32S5 23 5 13a7 7 0 0 1 14-1 7 7 0 0 1 14 1c0 10-14 19-14 19z" fill="#fff"/></svg></div>
      <p>安全</p>
    </div>
    <div class="feature">
      <div class="icon"><svg width="38" height="38" viewBox="0 0 38 38"><path d="M19 4l4.5 9.5 10 1.2-7.4 7 2 10.1L19 27l-9.1 4.8 2-10.1-7.4-7 10-1.2z" fill="#fff"/></svg></div>
      <p>抜群の効果</p>
    </div>
  </div>

  <svg class="usage-arc" width="226" height="110" viewBox="0 0 226 110">
    <defs><path id="usage-path" d="M18 104 A95 95 0 0 1 208 104"/></defs>
    <text font-family="M PLUS Rounded 1c, sans-serif" font-weight="700" font-size="17" fill="#2d9bcf"><textPath href="#usage-path" startOffset="50%" text-anchor="middle">簡単操作で誰でも楽々</textPath></text>
  </svg>
  <div class="usage-photo" role="img" aria-label="腕に脱毛機器を当てている写真"></div>

  <div class="contact-bar"></div>
  <div class="brand"><span class="dot"></span>Lumio ルミオ</div>
  <div class="contact">
    <p class="label">ご予約・お問い合わせ</p>
    <p class="tel"><svg width="24" height="24" viewBox="0 0 24 24"><path d="M6.6 10.8a15 15 0 0 0 6.6 6.6l2.2-2.2a1 1 0 0 1 1-.25 11 11 0 0 0 3.6.6 1 1 0 0 1 1 1V20a1 1 0 0 1-1 1A17 17 0 0 1 3 4a1 1 0 0 1 1-1h3.5a1 1 0 0 1 1 1 11 11 0 0 0 .6 3.6 1 1 0 0 1-.25 1z" fill="#2d9bcf"/></svg>0000-000-0000</p>
    <p class="address">住所ダミーの文章ダミーの文章</p>
  </div>
  <div class="map-box">MAPダミー</div>
</div>
</body>
</html>
```